" a empresa existe há 8 anos, é de 2 doutores que são casados, são cirurgioes e atendem alguns dias na semana em seus consultórios na clinica médica. o nome querem alterar, estão pensando, pois o 3o medico "b"nao existe mais. hoje eles utilizam uma foto de uma escultura em mármore que é uma familia em circulo. "

```html
<!DOCTYPE html>
<html lang="pt-BR">
<head>
<meta charset="UTF-8">
<title>Aurente – Papel Timbrado</title>
<link href="https://fonts.googleapis.com/css2?family=Marcellus&family=Open+Sans:wght@400;600&display=swap" rel="stylesheet">
<style>
  :root {
    --backdrop: #eeeae6;
    --paper: #ffffff;
    --teal: #4f8590;
    --teal-band: #6a949b;
    --rose: #d39c8a;
    --blush: #ecd3ca;
    --blush-faint: #f6e8e2;
    --ink: #5b5b5b;
  }
  * { margin: 0; padding: 0; box-sizing: border-box; }
  html, body { width: 1200px; height: 1200px; overflow: hidden; }
  body { background: var(--backdrop); position: relative; font-family: "Open Sans", sans-serif; }

  .letterhead {
    position: absolute; left: 300px; top: 176px;
    width: 600px; height: 848px;
    background: var(--paper);
    box-shadow: 0 6px 24px rgba(0,0,0,0.12);
    overflow: hidden;
  }

  .brand { position: absolute; left: 31px; top: 98px; }
  .brand-name {
    font-family: "Marcellus", serif;
    font-size: 42px; letter-spacing: 2px;
    color: var(--teal); line-height: 1;
  }
  .brand-tagline {
    margin-top: 8px;
    font-size: 7px; letter-spacing: 0.6px; text-transform: uppercase;
    color: var(--rose);
  }

  .brand-watermark {
    position: absolute; left: 30px; top: 600px;
    width: 280px; height: 200px;
    border-radius: 50%;
    background: radial-gradient(ellipse at center, var(--blush-faint) 0%, rgba(246,232,226,0.5) 55%, rgba(255,255,255,0) 75%);
  }

  .contact-list {
    position: absolute; right: 14px; top: 706px;
    list-style: none;
    font-size: 9.5px; color: var(--ink); text-align: right;
  }
  .contact-item {
    display: flex; justify-content: flex-end; align-items: center; gap: 6px;
    line-height: 1.25; margin-bottom: 9px;
  }
  .contact-item.address { align-items: center; }
  .contact-icon { width: 12px; height: 12px; flex: none; }

  .footer-band { position: absolute; left: 0; bottom: 0; width: 100%; height: 18px; display: flex; }
  .footer-band .band-blush { width: 335px; background: var(--blush); }
  .footer-band .band-teal { flex: 1; background: var(--teal-band); }
</style>
</head>
<body>
  <main class="letterhead">
    <header class="brand">
      <div class="brand-name">AURENTE</div>
      <div class="brand-tagline">Cirurgia Plástica e Medicina Estética</div>
    </header>

    <div class="brand-watermark" role="img" aria-label="Faint decorative brand mark in soft blush tones"></div>

    <ul class="contact-list">
      <li class="contact-item">
        <span>aurente@contato.com.br</span>
        <svg class="contact-icon" viewBox="0 0 12 12"><circle cx="6" cy="6" r="6" fill="#6a949b"/><rect x="3" y="4" width="6" height="4.2" fill="none" stroke="#fff" stroke-width="0.8"/><path d="M3 4 L6 6.3 L9 4" fill="none" stroke="#fff" stroke-width="0.8"/></svg>
      </li>
      <li class="contact-item">
        <span>(00) 99999-1234</span>
        <svg class="contact-icon" viewBox="0 0 12 12"><circle cx="6" cy="6" r="6" fill="#6a949b"/><rect x="4.2" y="2.8" width="3.6" height="6.4" rx="0.7" fill="none" stroke="#fff" stroke-width="0.8"/></svg>
      </li>
      <li class="contact-item">
        <span>www.aurente.com.br</span>
        <svg class="contact-icon" viewBox="0 0 12 12"><circle cx="6" cy="6" r="6" fill="#6a949b"/><circle cx="6" cy="6" r="3" fill="none" stroke="#fff" stroke-width="0.8"/><path d="M3 6 H9 M6 3 V9" stroke="#fff" stroke-width="0.6"/></svg>
      </li>
      <li class="contact-item address">
        <span>Rua Sem nome 00 Bairro Sem Nome<br>Cidade - Estado XXCep: 00.000-000</span>
        <svg class="contact-icon" viewBox="0 0 12 12"><circle cx="6" cy="6" r="6" fill="#6a949b"/><path d="M6 9.5 C4 7 3.8 6 3.8 5 A2.2 2.2 0 0 1 8.2 5 C8.2 6 8 7 6 9.5 Z" fill="#fff"/><circle cx="6" cy="5" r="0.8" fill="#6a949b"/></svg>
      </li>
    </ul>

    <div class="footer-band">
      <div class="band-blush"></div>
      <div class="band-teal"></div>
    </div>
  </main>
</body>
</html>
```